Velour Z, Premimum Quality Condom

Condom Package, 3 type, Ultra-Thin, Dotted, Anatomic,
Lubricated Latex Condom
this package box contain 3 foil packs of Condoms
I attached die line of Package box

```html
<!DOCTYPE html>
<html lang="en">
<head>
<meta charset="utf-8">
<title>Velour Z – Condom Box Dielines</title>
<link rel="stylesheet" href="https://fonts.googleapis.com/css2?family=Montserrat:wght@500;600&family=Josefin+Sans:wght@600&display=swap">
<style>
  :root {
    --bg-top: #e2d9da;
    --bg-bottom: #f7f5f6;
    --rose-gold: #eec3ad;
    --ink-light: #fbe6dc;
    --ink-white: #ffffff;
  }
  html, body {
    margin: 0;
    padding: 0;
    width: 1200px;
    height: 1064px;
    overflow: hidden;
  }
  .canvas {
    width: 1200px;
    height: 1064px;
    background: linear-gradient(180deg, var(--bg-top) 0%, var(--bg-bottom) 100%);
  }
  .dieline-sheet { display: block; width: 1200px; height: 1064px; }
  .die-cut { stroke: var(--rose-gold); stroke-width: 5; stroke-linejoin: round; }
  .fold-lines { fill: none; stroke: var(--rose-gold); stroke-width: 4; }
  .brand-name {
    font-family: "Montserrat", sans-serif;
    font-weight: 600;
    fill: var(--ink-light);
    text-anchor: middle;
  }
  .brand-name--front { font-size: 62px; letter-spacing: 4px; }
  .brand-name--back { font-size: 32px; letter-spacing: 2px; }
  .back-copy {
    font-family: "Montserrat", sans-serif;
    font-weight: 600;
    font-size: 11.5px;
    letter-spacing: 2.6px;
    fill: var(--ink-white);
    text-anchor: middle;
  }
  .front-copy {
    font-family: "Montserrat", sans-serif;
    font-weight: 600;
    font-size: 15px;
    letter-spacing: 4.5px;
    fill: var(--ink-white);
    text-anchor: middle;
  }
  .variant-name {
    font-family: "Josefin Sans", sans-serif;
    font-weight: 600;
    font-size: 22px;
    letter-spacing: 4px;
    fill: none;
    stroke: var(--ink-light);
    stroke-width: 1.2;
    text-anchor: middle;
  }
</style>
</head>
<body>
<main class="canvas">
  <svg class="dieline-sheet" viewBox="0 0 2044 1812" xmlns="http://www.w3.org/2000/svg">
    <defs>
      <linearGradient id="fill-ultra-thin" x1="0" y1="0" x2="1" y2="1">
        <stop offset="0" stop-color="#a87a86"/>
        <stop offset="0.22" stop-color="#d8b690"/>
        <stop offset="0.42" stop-color="#8c5cb6"/>
        <stop offset="0.6" stop-color="#7c58ab"/>
        <stop offset="0.78" stop-color="#9a7540"/>
        <stop offset="1" stop-color="#6c8a48"/>
      </linearGradient>
      <linearGradient id="fill-dotted" x1="0" y1="0" x2="0.4" y2="1">
        <stop offset="0" stop-color="#1d1a3c"/>
        <stop offset="0.45" stop-color="#3a2d55"/>
        <stop offset="0.75" stop-color="#7a5a48"/>
        <stop offset="1" stop-color="#a5804f"/>
      </linearGradient>
      <linearGradient id="fill-anatomic" x1="0" y1="0" x2="1" y2="1">
        <stop offset="0" stop-color="#3a12c8"/>
        <stop offset="0.35" stop-color="#2a0a8c"/>
        <stop offset="0.6" stop-color="#4b1ae0"/>
        <stop offset="1" stop-color="#0e0433"/>
      </linearGradient>

      <path id="die-outline" d="M100,145 L100,120 Q100,85 135,85 L418,85 Q453,85 453,120 L453,183 L528,183 L548,240 L548,265 L900,265 L900,240 L920,183 L995,183 L995,740 L975,805 L900,805 L900,863 Q900,898 865,898 L583,898 Q548,898 548,863 L548,805 L473,805 L453,745 L453,720 L100,720 L55,705 L55,280 L100,265 Z"/>
      <path id="die-folds" d="M100,145 H453 M55,265 H995 M55,720 H995 M100,265 V720 M453,145 V805 M548,183 V898 M900,183 V843 M548,843 H900"/>
    </defs>

    <!-- Ultra Thin box -->
    <g class="box box--ultra-thin">
      <use href="#die-outline" class="die-cut" fill="url(#fill-ultra-thin)" role="img" aria-label="Flowing abstract swirl in rose, gold, violet and olive tones"/>
      <use href="#die-folds" class="fold-lines"/>
      <text class="brand-name brand-name--back" x="277" y="440">Velour Z</text>
      <text class="back-copy" x="280" y="484">THIS BOX CONTAINS 3 PACKS OF "ULTRA</text>
      <text class="back-copy" x="280" y="513">THIN" LUBRICATED LATEX CONDOMS</text>
      <text class="back-copy" x="280" y="542">DESIGNED TO GUARANTEE SATISFACTION</text>
      <text class="back-copy" x="280" y="571">AND PROTECTION.</text>
      <text class="brand-name brand-name--front" x="728" y="430">Velour Z</text>
      <text class="front-copy" x="730" y="503">LUBRICATED LATEX CONDOM</text>
      <text class="front-copy" x="730" y="550">3 PACKS</text>
      <text class="variant-name" x="730" y="612">ULTRA THIN</text>
    </g>

    <!-- Dotted box -->
    <g class="box box--dotted" transform="translate(0 818)">
      <use href="#die-outline" class="die-cut" fill="url(#fill-dotted)" role="img" aria-label="Night sky with glowing golden particles and a warm light burst"/>
      <use href="#die-folds" class="fold-lines"/>
      <text class="brand-name brand-name--back" x="277" y="440">Velour Z</text>
      <text class="back-copy" x="280" y="484">THIS BOX CONTAINS 3 PACKS OF "DOTTED"</text>
      <text class="back-copy" x="280" y="513">LUBRICATED LATEX CONDOMS DESIGNED</text>
      <text class="back-copy" x="280" y="542">TO GUARANTEE SATISFACTION AND</text>
      <text class="back-copy" x="280" y="571">PROTECTION.</text>
      <text class="brand-name brand-name--front" x="728" y="430">Velour Z</text>
      <text class="front-copy" x="730" y="503">LUBRICATED LATEX CONDOM</text>
      <text class="front-copy" x="730" y="550">3 PACKS</text>
      <text class="variant-name" x="730" y="612">DOTTED</text>
    </g>

    <!-- Anatomic box -->
    <g class="box box--anatomic" transform="translate(1010 455)">
      <use href="#die-outline" class="die-cut" fill="url(#fill-anatomic)" role="img" aria-label="Swirling violet smoke on a deep indigo ground"/>
      <use href="#die-folds" class="fold-lines"/>
      <text class="brand-name brand-name--back" x="277" y="440">Velour Z</text>
      <text class="back-copy" x="280" y="484">THIS BOX CONTAINS 3 PACKS OF "ANATOMIC"</text>
      <text class="back-copy" x="280" y="513">LUBRICATED LATEX CONDOMS DESIGNED</text>
      <text class="back-copy" x="280" y="542">TO GUARANTEE SATISFACTION AND</text>
      <text class="back-copy" x="280" y="571">PROTECTION.</text>
      <text class="brand-name brand-name--front" x="728" y="430">Velour Z</text>
      <text class="front-copy" x="730" y="503">LUBRICATED LATEX CONDOM</text>
      <text class="front-copy" x="730" y="550">3 PACKS</text>
      <text class="variant-name" x="730" y="612">ANATOMIC</text>
    </g>
  </svg>
</main>
</body>
</html>
```